Labels for peptide supplements

I need editable label done as a template for a peptide brand Torvane Supplements to stick on the vials.
I need it done in two sizes:
3cm/6cm
2cm/4cm
I will attach some branding and a example label.

```html
<!DOCTYPE html>
<html lang="en">
<head>
<meta charset="utf-8">
<title>Torvane Supplements – Vial Labels</title>
<link href="https://fonts.googleapis.com/css2?family=Roboto+Condensed:wght@400;700&family=Michroma&family=Roboto:wght@400;700&display=swap" rel="stylesheet">
<style>
  :root {
    --canvas: #a9aaae;
    --size-title: #333333;
    --strip: #ffffff;
    --strip-text: #1a1a1a;
    --navy: #1b1a3d;
    --navy-deep: #161531;
    --teal: #0b3450;
    --violet-glow: rgba(120, 70, 170, 0.55);
    --text-light: #ffffff;
    --art-violet: #7b4fb8;
    --art-cyan: #4fb6dc;
    --art-orange: #f0904a;
  }
  * { box-sizing: border-box; margin: 0; padding: 0; }
  html, body { width: 1144px; height: 1200px; overflow: hidden; }
  body {
    background: var(--canvas);
    position: relative;
    font-family: "Roboto Condensed", "Arial Narrow", sans-serif;
  }
  .size-title {
    position: absolute;
    left: 0; width: 100%;
    text-align: center;
    font-family: "Roboto", Arial, sans-serif;
    font-weight: 400;
    color: var(--size-title);
    line-height: 1;
  }
  .size-title--large { top: 112px; font-size: 70px; }
  .size-title--small { top: 708px; font-size: 50px; }

  .label {
    position: absolute;
    display: flex;
  }
  .label--large { left: 109px; top: 198px; width: 926px; height: 462px; }
  .label--small { left: 263px; top: 771px; width: 618px; height: 308px; }

  .label__strip {
    background: var(--strip);
    position: relative;
    flex: none;
  }
  .label--large .label__strip { width: 115px; }
  .label--small .label__strip { width: 70px; }

  .label__expiry {
    position: absolute;
    top: 50%;
    font-family: "Roboto", Arial, sans-serif;
    font-weight: 700;
    color: var(--strip-text);
    white-space: nowrap;
    transform: translate(-50%, -50%) rotate(90deg);
  }
  .label--large .label__expiry { left: 44px; font-size: 15px; }
  .label--small .label__expiry { left: 22px; font-size: 9.5px; }

  .label__face {
    position: relative;
    flex: 1;
    overflow: hidden;
    background:
      radial-gradient(ellipse 42% 55% at 38% 48%, var(--violet-glow), transparent 70%),
      radial-gradient(ellipse 60% 70% at 95% 0%, var(--teal), transparent 75%),
      linear-gradient(180deg, var(--navy) 0%, var(--navy-deep) 100%);
  }

  .label__art {
    position: absolute;
    border-radius: 18px;
    background:
      radial-gradient(circle at 25% 35%, rgba(240,144,74,0.55), transparent 45%),
      radial-gradient(circle at 70% 45%, rgba(79,182,220,0.6), transparent 50%),
      radial-gradient(circle at 35% 80%, rgba(123,79,184,0.65), transparent 55%);
  }
  .label--large .label__art { left: 242px; top: 46px; width: 296px; height: 286px; }
  .label--small .label__art { left: 94px; top: 25px; width: 202px; height: 192px; }

  .label__brand {
    position: absolute;
    text-align: center;
    font-family: "Michroma", Arial, sans-serif;
    font-weight: 400;
    color: var(--text-light);
    text-transform: uppercase;
    line-height: 1.25;
    letter-spacing: 0.06em;
  }
  .label--large .label__brand { left: 236px; top: 348px; width: 310px; font-size: 22px; }
  .label--small .label__brand { left: 86px; top: 228px; width: 218px; font-size: 15px; }

  .label__info {
    position: absolute;
    color: var(--text-light);
    letter-spacing: -0.02em;
  }
  .label--large .label__info { left: 546px; top: 38px; width: 260px; font-size: 20px; line-height: 25px; }
  .label--small .label__info { left: 367px; top: 22px; width: 170px; font-size: 13.5px; line-height: 17px; }

  .label__info p { margin: 0; }
  .label--large .label__info .block + .block { margin-top: 6px; }
  .label--small .label__info .block + .block { margin-top: 4px; }

  .label__heading { font-weight: 700; }
  .label--large .label__heading { font-size: 24px; }
  .label--small .label__heading { font-size: 16px; }

  .label__origin { font-weight: 700; }
  .label--large .label__origin { margin-top: 12px !important; }
  .label--small .label__origin { margin-top: 8px !important; }
</style>
</head>
<body>

  <div class="size-title size-title--large">3X6</div>

  <section class="label label--large">
    <div class="label__strip">
      <span class="label__expiry">BEST EXP:</span>
    </div>
    <div class="label__face">
      <div class="label__art" role="img" aria-label="Illustration of a colourful DNA double helix beside a glowing molecule structure"></div>
      <div class="label__brand">Torvane<br>Supplements</div>
      <div class="label__info">
        <div class="block">
          <p>Store protected of light</p>
          <p>at no more than 86°F</p>
          <p>Keep out of reach of children</p>
          <p>Sale upon medical prescription</p>
        </div>
        <div class="block">
          <p><span class="label__heading">WARNINGS:</span> product of delicate</p>
          <p>use, which must be administrated</p>
          <p>under strict medical supervision</p>
          <p>Do not exceeded the prescribed</p>
          <p>dose</p>
        </div>
        <div class="block">
          <p class="label__heading">CONTRADICTIONS:</p>
          <p>Hypersensitivity to any of the</p>
          <p>components of the formula</p>
          <p>As indicated by a physician</p>
        </div>
        <div class="block label__origin">Manufactured in Australia</div>
      </div>
    </div>
  </section>

  <div class="size-title size-title--small">2x4</div>

  <section class="label label--small">
    <div class="label__strip">
      <span class="label__expiry">BEST EXP:</span>
    </div>
    <div class="label__face">
      <div class="label__art" role="img" aria-label="Illustration of a colourful DNA double helix beside a glowing molecule structure"></div>
      <div class="label__brand">Torvane<br>Supplements</div>
      <div class="label__info">
        <div class="block">
          <p>Store protected of light</p>
          <p>at no more than 86°F</p>
          <p>Keep out of reach of children</p>
          <p>Sale upon medical prescription</p>
        </div>
        <div class="block">
          <p><span class="label__heading">WARNINGS:</span> product of delicate</p>
          <p>use, which must be administrated</p>
          <p>under strict medical supervision</p>
          <p>Do not exceeded the prescribed</p>
          <p>dose</p>
        </div>
        <div class="block">
          <p class="label__heading">CONTRADICTIONS:</p>
          <p>Hypersensitivity to any of the</p>
          <p>components of the formula</p>
          <p>As indicated by a physician</p>
        </div>
        <div class="block label__origin">Manufactured in Australia</div>
      </div>
    </div>
  </section>

</body>
</html>
```